Banner Ad Design Project

I need a banner design for a new application which is going to the displayed on the TradeBazaar.

The banner is needed for this application:
https://portal.brivanta-cloud.example/tradebazaar/entryView?entryRef=k7Q84000002mxpdBRT

Example banners can be found here:
https://portal.brivanta-cloud.example/tradebazaar/entryView?entryRef=k7Q84000006hzswBRT

Or
https://portal.brivanta-cloud.example/tradebazaar/entryView?entryRef=k7Q84000002wLMRBR5

Target Market(s)

Enterprise business.

Requirements
Must have
• Must include our pendrowix logo.

```html
<!DOCTYPE html>
<html lang="en">
<head>
<meta charset="utf-8">
<title>Approval History Reporting – Banner Variants</title>
<link rel="stylesheet" href="https://fonts.googleapis.com/css2?family=Questrial&family=Nunito+Sans:wght@800&display=swap">
<style>
  :root {
    --page-bg: #ffffff;
    --frame: #1a1a1a;
    --panel-white: #ffffff;
    --panel-shadow: rgba(0, 0, 0, 0.35);
    --title: #ffffff;
    --tagline: #3c3c3c;
    --cube-top: #555555;
    --cube-left: #3c3c3c;
    --cube-right: #2a2a2a;
    --brand-name: #f0963a;
    --brand-dot: #4a7fc8;
    --blue-a: #3f93dc;
    --blue-b: #7cc4f6;
    --pink-a: #d24f9c;
    --pink-b: #f36fca;
    --orange-a: #dd8c48;
    --orange-b: #f4ab70;
  }
  * { box-sizing: border-box; margin: 0; padding: 0; }
  html, body { width: 1200px; height: 800px; overflow: hidden; background: var(--page-bg); }
  .canvas { position: relative; width: 1200px; height: 800px; }

  .banner {
    position: absolute;
    left: 133px;
    width: 930px;
    height: 80px;
    border: 1px solid var(--frame);
    overflow: hidden;
  }
  .banner--blue   { top: 101px; background: linear-gradient(90deg, var(--blue-a), var(--blue-b)); }
  .banner--pink   { top: 336px; background: linear-gradient(90deg, var(--pink-a), var(--pink-b)); }
  .banner--orange { top: 565px; background: linear-gradient(90deg, var(--orange-a), var(--orange-b)); }

  .brand-panel {
    position: absolute;
    left: 0;
    top: 0;
    width: 206px;
    height: 78px;
    background: var(--panel-white);
    box-shadow: 4px 0 6px var(--panel-shadow);
  }

  .brand {
    position: absolute;
    left: 18px;
    top: 0;
    height: 78px;
    display: flex;
    align-items: center;
    gap: 28px;
  }
  .brand__dot { width: 44px; height: 44px; border-radius: 50%; background: var(--brand-dot); }
  .brand__name {
    font-family: "Questrial", sans-serif;
    font-size: 17px;
    color: var(--brand-name);
  }

  .headline {
    position: absolute;
    left: 195px;
    width: 600px;
    top: 2px;
    text-align: center;
  }
  .headline__title {
    font-family: "Questrial", sans-serif;
    font-weight: 400;
    font-size: 40px;
    line-height: 46px;
    color: var(--title);
    letter-spacing: 1px;
    white-space: nowrap;
  }
  .headline__tagline {
    font-family: "Nunito Sans", sans-serif;
    font-weight: 800;
    font-size: 20px;
    line-height: 24px;
    letter-spacing: 0.4px;
    color: var(--tagline);
    display: flex;
    justify-content: center;
    align-items: center;
    gap: 8px;
    white-space: nowrap;
  }
  .cube { width: 18px; height: 18px; }
  .cube__top { fill: var(--cube-top); }
  .cube__left { fill: var(--cube-left); }
  .cube__right { fill: var(--cube-right); }

  .plane-art {
    position: absolute;
    left: 778px;
    top: 6px;
    width: 120px;
    height: 66px;
    border-radius: 40% 10% 40% 20%;
    background: linear-gradient(200deg, rgba(255,255,255,0.95), rgba(255,255,255,0.55) 60%, rgba(255,255,255,0.1));
  }
</style>
</head>
<body>
<div class="canvas">

  <section class="banner banner--blue">
    <div class="brand-panel"></div>
    <div class="brand"><span class="brand__dot"></span><span class="brand__name">Pendrowix</span></div>
    <div class="headline">
      <h1 class="headline__title">Approval History Reporting</h1>
      <p class="headline__tagline">Monitoring
        <svg class="cube" viewBox="0 0 16 16" aria-hidden="true"><path class="cube__top" d="M8 1 L15 4.5 L8 8 L1 4.5 Z"/><path class="cube__left" d="M1 5.5 L7.4 8.8 V15.5 L1 12 Z"/><path class="cube__right" d="M15 5.5 L8.6 8.8 V15.5 L15 12 Z"/></svg>
        Tracking
        <svg class="cube" viewBox="0 0 16 16" aria-hidden="true"><path class="cube__top" d="M8 1 L15 4.5 L8 8 L1 4.5 Z"/><path class="cube__left" d="M1 5.5 L7.4 8.8 V15.5 L1 12 Z"/><path class="cube__right" d="M15 5.5 L8.6 8.8 V15.5 L15 12 Z"/></svg>
        Approving</p>
    </div>
    <div class="plane-art" role="img" aria-label="White paper plane illustration"></div>
  </section>

  <section class="banner banner--pink">
    <div class="brand-panel"></div>
    <div class="brand"><span class="brand__dot"></span><span class="brand__name">Pendrowix</span></div>
    <div class="headline">
      <h1 class="headline__title">Approval History Reporting</h1>
      <p class="headline__tagline">Monitoring
        <svg class="cube" viewBox="0 0 16 16" aria-hidden="true"><path class="cube__top" d="M8 1 L15 4.5 L8 8 L1 4.5 Z"/><path class="cube__left" d="M1 5.5 L7.4 8.8 V15.5 L1 12 Z"/><path class="cube__right" d="M15 5.5 L8.6 8.8 V15.5 L15 12 Z"/></svg>
        Tracking
        <svg class="cube" viewBox="0 0 16 16" aria-hidden="true"><path class="cube__top" d="M8 1 L15 4.5 L8 8 L1 4.5 Z"/><path class="cube__left" d="M1 5.5 L7.4 8.8 V15.5 L1 12 Z"/><path class="cube__right" d="M15 5.5 L8.6 8.8 V15.5 L15 12 Z"/></svg>
        Approving</p>
    </div>
    <div class="plane-art" role="img" aria-label="Pale pink paper plane illustration"></div>
  </section>

  <section class="banner banner--orange">
    <div class="brand-panel"></div>
    <div class="brand"><span class="brand__dot"></span><span class="brand__name">Pendrowix</span></div>
    <div class="headline">
      <h1 class="headline__title">Approval History Reporting</h1>
      <p class="headline__tagline">Monitoring
        <svg class="cube" viewBox="0 0 16 16" aria-hidden="true"><path class="cube__top" d="M8 1 L15 4.5 L8 8 L1 4.5 Z"/><path class="cube__left" d="M1 5.5 L7.4 8.8 V15.5 L1 12 Z"/><path class="cube__right" d="M15 5.5 L8.6 8.8 V15.5 L15 12 Z"/></svg>
        Tracking
        <svg class="cube" viewBox="0 0 16 16" aria-hidden="true"><path class="cube__top" d="M8 1 L15 4.5 L8 8 L1 4.5 Z"/><path class="cube__left" d="M1 5.5 L7.4 8.8 V15.5 L1 12 Z"/><path class="cube__right" d="M15 5.5 L8.6 8.8 V15.5 L15 12 Z"/></svg>
        Approving</p>
    </div>
    <div class="plane-art" role="img" aria-label="Cream paper plane illustration"></div>
  </section>

</div>
</body>
</html>
```